11X17 Poster Drop A Dress Size Challenge

We are having a 21-Day Drop A Dress Size Challenge for our Fitness Studio. We need a poster designed using the template attached as a reference. I have included our Vorenzo Bootcamps logo to put in the poster as well. Please DO NOT use the graphics in the flyer as we are expecting something much better :)
- Size needed 11x17 with bleeding for printing
- We need this made in Photoshop (CS3 friendly) or at least delivered in PS as we might change some text or re-arrange the design later on.

Target Market(s)

Personal Training Studio

Industry/Entity Type

Printing

Colors
0255a3
3377b5
85acd3
f37123
f68e4e
faa54b
f78f20
0692cd
34a7d8

Requirements
Must have
• Must be 11x17 with bleed for printing
• Must be in PS file (CS3 compatible)
• Must include our Vorenzo Bootcamps logo somewhere in the poster
• Must include the information provided in the attached flyer
Nice to have
• Nice to have quality graphics that coincide with the challenge and our logo
Should not have
• Please NO scantily dressed women :)

```html
<!DOCTYPE html>
<html lang="en">
<head>
<meta charset="utf-8">
<title>Drop A Dress Size in 21 Days – Poster</title>
<link rel="stylesheet" href="https://fonts.googleapis.com/css2?family=Barlow+Semi+Condensed:wght@400;500;600;700&family=Barlow:wght@400;500;600;700&display=swap">
<style>
  :root {
    --navy: #1f3a6e;
    --blue-deep: #0255a3;
    --blue: #3377b5;
    --blue-bright: #34a7d8;
    --blue-soft: #85acd3;
    --ribbon: #3f93cf;
    --panel: rgba(52, 119, 181, 0.62);
    --white: #ffffff;
    --page: #ffffff;
    --shade: #4b5668;
  }
  * { margin: 0; padding: 0; box-sizing: border-box; }
  html, body { width: 1200px; height: 900px; overflow: hidden; background: var(--page); }
  body { position: relative; font-family: "Barlow", Arial, sans-serif; }

  .poster {
    position: absolute; left: 325px; top: 25px;
    width: 550px; height: 850px; overflow: hidden;
    color: var(--white);
  }
  .poster__photo {
    position: absolute; inset: 0;
    background:
      linear-gradient(90deg, rgba(231,150,130,0.75) 0 8%, transparent 14%),
      radial-gradient(ellipse 30% 45% at 62% 38%, #d7b9a8 0%, rgba(215,185,168,0) 70%),
      linear-gradient(180deg, #c9d9ec 0%, #e6eef6 22%, #bcd0e6 45%, #8ea6c3 65%, #6f7f96 85%, #555f70 100%);
  }
  .poster__shapes { position: absolute; inset: 0; }

  .headline {
    position: absolute; left: 51px; top: 22px; width: 226px;
    font-family: "Barlow Semi Condensed", Arial, sans-serif;
    font-weight: 500; text-align: center; line-height: 0.92;
  }
  .headline__line { display: block; }
  .headline__line--a { font-size: 62px; }
  .headline__line--b { font-size: 66px; font-weight: 600; }
  .headline__line--c { font-size: 86px; font-weight: 600; }
  .headline__line--d { font-size: 36px; margin-top: 6px; }

  .offer { position: absolute; left: 303px; top: 18px; color: var(--navy); font-weight: 700; }
  .offer__title { font-size: 23px; line-height: 1.1; }
  .offer__price { font-size: 16px; line-height: 1.1; }

  .urgency { position: absolute; left: 13px; top: 366px; width: 300px; text-align: center; }
  .urgency__hurry { font-family: "Barlow Semi Condensed", Arial, sans-serif; font-size: 34px; font-weight: 500; line-height: 1; }
  .urgency__limited { font-family: "Barlow Semi Condensed", Arial, sans-serif; font-size: 17px; font-weight: 500; margin-top: 2px; }
  .urgency__date { color: var(--navy); font-size: 24px; font-weight: 700; margin-top: 6px; }

  .pitch {
    position: absolute; left: 52px; top: 486px; width: 226px;
    font-size: 12.6px; font-weight: 600; line-height: 1.36;
  }
  .pitch p + p { margin-top: 14px; }

  .benefits { position: absolute; left: 290px; top: 480px; width: 252px; }
  .benefits__title { font-size: 21px; font-weight: 600; line-height: 1.2; margin-bottom: 22px; }
  .benefits__item { font-size: 9.6px; line-height: 12px; margin-bottom: 5px; }
  .benefits__item strong { font-weight: 700; }
  .benefits__value { font-size: 11px; line-height: 13px; font-weight: 600; margin-top: 8px; }

  .contact { position: absolute; left: 300px; top: 692px; }
  .contact__phone { font-size: 24px; font-weight: 600; line-height: 1.1; }
  .contact__web { font-size: 14.5px; font-weight: 600; line-height: 1.3; }

  .brand {
    position: absolute; left: 298px; top: 745px; width: 226px; height: 70px;
    display: flex; align-items: center; justify-content: center; gap: 10px;
    background: var(--white);
  }
  .brand__mark { width: 16px; height: 16px; background: var(--blue-deep); }
  .brand__name { font-size: 20px; font-weight: 700; color: var(--blue-deep); }

  .prize {
    position: absolute; left: 38px; top: 776px; width: 250px;
    text-align: center; font-family: "Barlow Semi Condensed", Arial, sans-serif;
    font-size: 12px; font-weight: 500; line-height: 1.3; letter-spacing: 0.3px;
  }
  .prize small { font-size: 10px; }
</style>
</head>
<body>
  <main class="poster">
    <div class="poster__photo" role="img" aria-label="Photo of a smiling woman in a summer dress walking through a bright shopping mall"></div>

    <svg class="poster__shapes" width="550" height="850" viewBox="0 0 550 850" aria-hidden="true">
      <polygon points="51,0 277,0 277,232 164,275 51,232" fill="var(--ribbon)" opacity="0.95"/>
      <rect x="0" y="460" width="550" height="223" fill="var(--panel)"/>
      <rect x="0" y="683" width="550" height="167" fill="var(--shade)" opacity="0.55"/>
      <polygon points="51,460 277,460 277,690 164,735 51,690" fill="var(--blue-bright)" opacity="0.9"/>
    </svg>

    <h1 class="headline">
      <span class="headline__line headline__line--a">DROP A</span>
      <span class="headline__line headline__line--b">DRESS</span>
      <span class="headline__line headline__line--c">SIZE</span>
      <span class="headline__line headline__line--d">IN 21 DAYS</span>
    </h1>

    <div class="offer">
      <p class="offer__title">Claim your spot NOW</p>
      <p class="offer__price">Classes ONLY $97 SAVE $230</p>
    </div>

    <div class="urgency">
      <p class="urgency__hurry">HURRY!</p>
      <p class="urgency__limited">SPACE IS LIMITED LADIES!!!</p>
      <p class="urgency__date">Starts April 6th 2015</p>
    </div>

    <div class="pitch">
      <p>Are you tired of all the health clubs and fitness centers that tell you exactly what you want to hear to get you to join, but once you’re a member they forget about you and don’t teach you anything about how to get results?</p>
      <p>Are you frustrated by all the gimmicks; the pills, powders, shakes and gadgets sold on late night TV that are nothing more than empty promises and slick marketing?</p>
    </div>

    <section class="benefits">
      <h2 class="benefits__title">Here’s what you get:</h2>
      <p class="benefits__item"><strong>Three weeks</strong> worth of <strong>Fat Burning Workouts</strong> with a Certified Personal Trainer to make sure that you don’t spend one minute exercising that doesn’t produce results.</p>
      <p class="benefits__item"><strong>21 Days of Fat Burning Meal Plans</strong> designed by a Registered Dietician to ensure that you reach your goals as quickly as possible.</p>
      <p class="benefits__item"><strong>Nutrition Coaching Session</strong> to answer all your questions and set you up for success</p>
      <p class="benefits__item"><strong>21 Days of Lessons</strong> to keep you on track to achieving your goal of dropping a dress size</p>
      <p class="benefits__value">You get all this – a $327 Value – for ONLY $97!</p>
    </section>

    <div class="contact">
      <p class="contact__phone">Call 303-555-0148</p>
      <p class="contact__web">www.vorenzobootcamps.com</p>
    </div>

    <div class="brand">
      <span class="brand__mark"></span>
      <span class="brand__name">Vorenzo Bootcamps</span>
    </div>

    <p class="prize">WINNER GETS $100 Cash,<br>A NEW DRESS <small>(Up to $100 Value)</small><br>AND A FREE PHOTO SHOOT! <small>($150 Value)</small></p>
  </main>
</body>
</html>
```